Brenway Productions photography and video creator

I need a business card for my production company. I shoot photography and videography for real estate, adventure sports and businesses

simple not to busy

Colors

Designer to choose colors to be used in the design.

Requirements
Must have
• dara@brenwayproductions.ca
• phone -5803317264
• instagram dara_brenway

```html
<!DOCTYPE html>
<html lang="en">
<head>
<meta charset="UTF-8">
<title>Brenway Productions – Business Card</title>
<link rel="stylesheet" href="https://fonts.googleapis.com/css2?family=Lato:wght@300;400;700;900&display=swap">
<style>
  :root {
    --backdrop: #2b2b2c;
    --card: #1f2022;
    --ink: #ffffff;
    --ink-soft: #e4e4e4;
    --rule: #6d6e70;
    --mark-light: #c9cacc;
    --mark-mid: #8f9194;
    --mark-dark: #3a3b3d;
    --pattern-dark: #1c1d1f;
    --pattern-mid: #2a2b2e;
    --pattern-light: #34353a;
  }
  * { margin: 0; padding: 0; box-sizing: border-box; }
  html, body {
    width: 1200px;
    height: 1108px;
    overflow: hidden;
    background: var(--backdrop);
    font-family: "Lato", sans-serif;
  }
  .canvas {
    width: 1200px;
    height: 1108px;
    display: flex;
    align-items: center;
    justify-content: center;
    gap: 60px;
  }
  .card {
    width: 420px;
    height: 640px;
    border-radius: 26px;
    background: var(--card);
    box-shadow: 0 18px 40px rgba(0,0,0,0.45);
    position: relative;
    overflow: hidden;
  }
  .card-front {
    display: flex;
    flex-direction: column;
    align-items: center;
    padding-top: 52px;
    color: var(--ink);
  }
  .brand {
    display: flex;
    flex-direction: column;
    align-items: center;
    gap: 16px;
  }
  .brand-circle {
    width: 170px;
    height: 170px;
    border-radius: 50%;
    background: linear-gradient(180deg, var(--mark-light) 0%, var(--mark-mid) 45%, var(--mark-dark) 75%, #111214 100%);
  }
  .brand-name {
    font-weight: 700;
    font-size: 22px;
    letter-spacing: 4px;
    text-transform: uppercase;
    color: var(--ink);
  }
  .person-name {
    margin-top: 46px;
    font-weight: 700;
    font-size: 30px;
    letter-spacing: 0.5px;
    text-transform: uppercase;
  }
  .icon-rule {
    margin-top: 16px;
    width: 300px;
    display: flex;
    align-items: center;
    gap: 8px;
  }
  .icon-rule .line { flex: 1; height: 1px; background: var(--rule); }
  .contact-icon {
    width: 24px;
    height: 24px;
    border-radius: 50%;
    background: var(--ink);
    display: flex;
    align-items: center;
    justify-content: center;
  }
  .contact-list {
    margin-top: 12px;
    list-style: none;
    text-align: center;
    font-size: 21px;
    line-height: 1.3;
    color: var(--ink-soft);
    font-weight: 400;
  }
  .contact-rule {
    margin-top: 14px;
    width: 300px;
    height: 1px;
    background: var(--rule);
  }
  .social {
    margin-top: 16px;
    font-size: 21px;
    color: var(--ink-soft);
  }
  .social strong { font-weight: 700; }

  .card-back .pattern {
    position: absolute;
    inset: 0;
    background:
      radial-gradient(ellipse 70% 45% at 55% 25%, var(--pattern-light) 0%, transparent 70%),
      radial-gradient(ellipse 60% 40% at 35% 70%, var(--pattern-mid) 0%, transparent 70%),
      linear-gradient(160deg, var(--pattern-mid) 0%, var(--pattern-dark) 80%);
  }
  .back-mark {
    position: absolute;
    left: 0;
    right: 0;
    top: 420px;
    display: flex;
    flex-direction: column;
    align-items: center;
    gap: 12px;
  }
  .back-mark .dot {
    width: 34px;
    height: 34px;
    border-radius: 50%;
    background: var(--ink);
  }
  .back-mark .name {
    font-weight: 700;
    font-size: 18px;
    letter-spacing: 4px;
    text-transform: uppercase;
    color: var(--ink);
  }
</style>
</head>
<body>
<main class="canvas">
  <section class="card card-front" aria-label="Card front">
    <div class="brand">
      <div class="brand-circle" role="img" aria-label="Round mountain and pine forest scene in greys"></div>
      <div class="brand-name">Brenway Productions</div>
    </div>
    <h1 class="person-name">Dara Brenway</h1>
    <div class="icon-rule">
      <span class="line"></span>
      <span class="contact-icon" aria-label="Phone">
        <svg width="14" height="14" viewBox="0 0 24 24"><path fill="#1f2022" d="M6.6 10.8a15 15 0 0 0 6.6 6.6l2.2-2.2a1 1 0 0 1 1-.25 11.4 11.4 0 0 0 3.6.57 1 1 0 0 1 1 1V20a1 1 0 0 1-1 1A17 17 0 0 1 3 4a1 1 0 0 1 1-1h3.5a1 1 0 0 1 1 1c0 1.25.2 2.45.57 3.57a1 1 0 0 1-.25 1z"/></svg>
      </span>
      <span class="contact-icon" aria-label="Email">
        <svg width="14" height="14" viewBox="0 0 24 24"><rect x="3" y="6" width="18" height="12" fill="none" stroke="#1f2022" stroke-width="2"/><path d="M3 6l9 7 9-7" fill="none" stroke="#1f2022" stroke-width="2"/></svg>
      </span>
      <span class="contact-icon" aria-label="Website">
        <svg width="14" height="14" viewBox="0 0 24 24"><circle cx="12" cy="12" r="9" fill="none" stroke="#1f2022" stroke-width="2"/><ellipse cx="12" cy="12" rx="4" ry="9" fill="none" stroke="#1f2022" stroke-width="1.6"/><path d="M3 12h18" stroke="#1f2022" stroke-width="1.6"/></svg>
      </span>
      <span class="line"></span>
    </div>
    <ul class="contact-list">
      <li>5803317264</li>
      <li>dara@brenwayproductions.ca</li>
      <li>www.brenwayproductions.ca</li>
    </ul>
    <div class="contact-rule"></div>
    <p class="social"><strong>INSTAGRAM:</strong> dara_brenway</p>
  </section>

  <section class="card card-back" aria-label="Card back">
    <div class="pattern" role="img" aria-label="Faint repeating pine tree pattern on dark background"></div>
    <div class="back-mark">
      <span class="dot"></span>
      <span class="name">Brenway Productions</span>
    </div>
  </section>
</main>
</body>
</html>
```